Wordpress web design

We need a website buil in using Wordpress with 5 pages.

Pages: HOME SERVICES GALLERY TESTIMONIALS CONTACT US ABOUT US.

We are looking for a unique, professional and clean web for our construction company.

Company name: TALL OAK BUILDING SERVICES. We can olso provide you with the logo. Please don't use any flashin, intro, or any ready templates.

All your ideas are welcome.

Many thanks,
Dorian

Target Market(s)

Construction

Industry/Entity Type

Construction

Font styles to use
Sans Serif
Decorative

Requirements
Must have
• Connect with construction and London
Nice to have
• Nice and clean

```html
<!DOCTYPE html>
<html lang="en">
<head>
<meta charset="utf-8">
<title>Tall Oak Building Services</title>
<link href="https://fonts.googleapis.com/css2?family=Cinzel:wght@400;700&family=Lato:ital,wght@0,400;0,700;1,400&display=swap" rel="stylesheet">
<style>
:root{
  --red:#d7141a;
  --blue:#1e9fe0;
  --blue-dark:#1587c4;
  --ink:#222;
  --text:#444;
  --beige:#efede8;
  --gray-bg:#dcdad6;
  --white:#fff;
  --dark:#2a2a2a;
}
*{margin:0;padding:0;box-sizing:border-box}
html,body{width:827px;height:1200px;overflow:hidden}
body{position:relative;background:var(--white);font-family:'Lato',sans-serif;color:var(--text)}
.abs{position:absolute}
.head-band{left:0;top:0;width:827px;height:346px;background:linear-gradient(90deg,#cfccc7,#ecebe8 30%,#ecebe8 70%,#cfccc7)}
.frame{left:90px;top:0;width:647px;height:346px;background:var(--red)}
.topbar{left:95px;top:0;width:637px;height:66px;background:linear-gradient(#fafafa,#eef0f5)}
.brand{left:104px;top:24px;font-family:'Cinzel',serif;font-weight:700;font-size:13px;color:var(--ink);display:flex;align-items:center;gap:6px}
.brand .dot{width:12px;height:12px;background:var(--red)}
.phone{left:614px;top:11px;font-size:12px;color:#333;display:flex;align-items:center;gap:5px}
.nav{left:274px;top:41px;display:flex;font-family:'Cinzel',serif;font-size:11px;color:#333;letter-spacing:.5px}
.nav span{padding:0 7px;border-left:1px solid #aaa;line-height:11px}
.nav span:first-child{border:0;padding-left:0;color:var(--red)}
.hero{left:95px;top:66px;width:637px;height:278px;background:linear-gradient(#6d7e96 0%,#a7b1bd 35%,#8b8175 60%,#4d6a33 85%,#3e5a2a)}
.caption{left:464px;top:262px;width:262px;height:50px;background:rgba(20,20,20,.85);padding:4px 6px;font-family:'Cinzel',serif;font-size:17px;line-height:22px;color:var(--white)}
.caption em{font-style:normal;color:#2eb3f2;display:block}
.dots{left:664px;top:324px;display:flex;gap:5px}
.dots i{width:8px;height:8px;border-radius:50%;background:#ccc;display:block}
.dots i.on{background:var(--red);border:1px solid #fff}
.services{left:0;top:346px;width:827px;height:274px;background:linear-gradient(#f3f2ef,#ebe9e4)}
.card{top:381px;width:200px;height:193px;background:#fafafa;border:1px solid #c9c7c2;border-radius:3px;box-shadow:0 4px 6px rgba(0,0,0,.12);padding:6px}
.card .ph{height:90px}
.card h3{font-family:'Cinzel',serif;font-weight:400;font-size:14px;color:var(--blue);margin:6px 2px 0;padding-bottom:5px;border-bottom:1px dotted #bbb}
.card p{font-size:9px;line-height:13px;color:#333;margin:6px 2px 0;padding-bottom:6px;border-bottom:1px dotted #bbb}
.card a{display:block;font-size:9px;color:var(--red);margin:8px 3px 0;text-decoration:none}
.rule{left:120px;top:598px;width:590px;height:1px;background:#cfcdc8}
.welcome{left:92px;top:634px;width:432px}
.welcome h2{font-family:'Cinzel',serif;font-weight:400;font-size:17px;color:var(--ink);padding-bottom:4px;border-bottom:1px solid #ccc}
.welcome h2 em{font-style:normal;color:var(--blue)}
.welcome .lead{font-weight:700;font-size:9.5px;line-height:15px;color:#222;margin-top:6px}
.welcome p{font-size:9.5px;line-height:15.6px;color:#333;margin-top:3px}
.welcome a{display:block;font-size:9.5px;font-weight:700;color:var(--red);margin-top:6px;text-decoration:none}
.testi{left:556px;top:634px;width:181px}
.testi h2{font-family:'Cinzel',serif;font-weight:400;font-size:17px;color:var(--blue);padding-bottom:4px;border-bottom:1px solid #ccc;display:flex;align-items:center;gap:7px}
.avatar{left:556px;top:662px;width:60px;height:60px;border-radius:50%;background:linear-gradient(#c9a58a,#7a6a5e);border:3px solid #ddd}
.person{left:628px;top:680px;font-size:10px;color:#222}
.person small{display:block;font-size:8.5px;color:#555;margin-top:3px}
.quote{left:556px;top:732px;width:181px;height:74px;border:1px solid #e2e2e2;background:#fcfcfc;padding:8px 8px;font-style:italic;font-size:9px;line-height:15.5px;color:#444}
.qdots{left:696px;top:793px;display:flex;gap:3px}
.qdots i{width:5px;height:5px;border-radius:50%;background:#ccc;display:block}
.qdots i.on{background:var(--red)}
.gallery{left:0;top:834px;width:827px;height:172px;background:#eceae6;border-top:1px solid #d6d4cf}
.tab{left:310px;top:834px;width:210px;height:24px;background:linear-gradient(#8a8a8a,#5c5c5c);clip-path:polygon(0 0,100% 0,93% 100%,7% 100%);font-family:'Cinzel',serif;font-size:15px;color:var(--white);text-align:center;line-height:24px;letter-spacing:.5px}
.shot{top:883px;width:141px;height:97px}
.shot .label{position:absolute;left:0;right:0;bottom:0;height:25px;background:rgba(0,0,0,.7);color:#fff;font-size:10px;line-height:25px;padding-left:7px}
.arrow{top:921px;width:19px;height:19px;border-radius:50%;border:1.5px solid #aaa;display:flex;align-items:center;justify-content:center}
.footer{left:0;top:1006px;width:827px;height:194px;background:linear-gradient(var(--blue) 0 40px,#29a8e6 40px)}
.fline{left:0;top:1046px;width:827px;border-top:1px dashed #0e6fa3}
.fh{top:1019px;font-family:'Cinzel',serif;font-size:13px;color:var(--white);letter-spacing:.5px}
.social{left:616px;top:1014px;display:flex;gap:6px}
.social i{width:21px;height:21px;border-radius:50%;display:block;border:1.5px solid #fff}
.vsep{top:1052px;width:1px;height:140px;background:#1a8cc6}
.links{left:90px;top:1057px;list-style:none;font-size:9px;color:#fff}
.links li{height:23.3px}
.links li::before{content:"›";margin-right:8px}
.cdet{left:240px;top:1057px;font-size:9px;line-height:14px;color:#fff}
.cdet b{font-weight:700}
.crow{left:238px;font-size:9px;color:#fff;display:flex;align-items:center;gap:5px}
.field{left:402px;width:152px;height:20px;background:#bfe6fb;border:1px solid #0f6fa5;font-size:9px;color:#333;padding:3px 6px}
.submit{left:402px;top:1164px;width:68px;height:19px;background:#3b3b3b;color:#fff;font-size:10px;font-weight:700;text-align:center;line-height:19px;border:1px solid #222}
.fbrand{left:586px;top:1090px;width:162px;text-align:center;font-family:'Cinzel',serif;font-weight:700;font-size:14px;color:#fff}
.copy{left:586px;top:1161px;width:162px;text-align:center;font-size:9px;line-height:13px;color:#fff}
</style>
</head>
<body>
<div class="abs head-band"></div>
<div class="abs frame"></div>
<div class="abs topbar"></div>
<div class="abs brand"><span class="dot"></span>TALL OAK</div>
<div class="abs phone">
  <svg width="18" height="18" viewBox="0 0 18 18"><circle cx="9" cy="9" r="8" fill="none" stroke="#333" stroke-width="1.4"/><path d="M6 5l2 0 1 2-1 1 2 2 1-1 2 1 0 2c-4 0-7-3-7-7z" fill="#333"/></svg>
  123-555-0142
</div>
<div class="abs nav"><span>Home</span><span>Services</span><span>Gallery</span><span>Testimonials</span><span>About Us</span><span>Contact Us</span></div>
<div class="abs hero" role="img" aria-label="Large two-storey family house with lit windows and a green front lawn at dusk"></div>
<div class="abs caption">WE ARE A FULL SERVICE<em>CONSTRUCTION COMPANY</em></div>
<div class="abs dots"><i class="on"></i><i></i><i></i><i></i></div>

<div class="abs services"></div>
<div class="abs card" style="left:91px">
  <div class="ph" role="img" aria-label="Suburban family home" style="background:linear-gradient(#7fb0de,#d9cfb6 55%,#5b7a3a)"></div>
  <h3>Residential Projects</h3>
  <p>Lorem ipsum dolor sit amet, consectetuer adipiscing elit, sed diam Lorem ipsum</p>
  <a>Read More »</a>
</div>
<div class="abs card" style="left:314px">
  <div class="ph" role="img" aria-label="Glass office towers against blue sky" style="background:linear-gradient(120deg,#3a5f8f,#7ba6d4 50%,#3f6b2e)"></div>
  <h3>Commercial Projects</h3>
  <p>Lorem ipsum dolor sit amet, consectetuer adipiscing elit, sed diam Lorem ipsum</p>
  <a>Read More &gt;&gt;</a>
</div>
<div class="abs card" style="left:537px">
  <div class="ph" role="img" aria-label="Builders reviewing plans on a construction site" style="background:linear-gradient(#c89a52,#8a7a66 50%,#d8d2c6)"></div>
  <h3>Property Management</h3>
  <p>Lorem ipsum dolor sit amet, consectetuer adipiscing elit, sed diam Lorem ipsum</p>
  <a>Read More &gt;&gt;</a>
</div>
<div class="abs rule"></div>

<div class="abs welcome">
  <h2>Welcome to <em>Tall Oak Building Services</em></h2>
  <p class="lead">Lorem ipsum dolor sit amet, consectetuer adipiscing elit, sed diam nonummy nibh euismod tincidl untm ut laoreet dolore magna aliquam erat volutpat.</p>
  <p>Lorem ipsum dolor sit amet, consectetuer adipiscing elit, sed diam nonummy nibh euismod tinciduntm ut laoreet dolore magna aliquam erat volutpat. Ut wisi enim ad minim veniam, quis nostrud exerciosgi tation ullamcorper suscipit lobortis nisl ut aliquip ex ea commodo consequat. Duis autem vel eumsodn iriure dolor in hendrerit in vulputate velit esse molestie consequat, vel illum dolore eu feugiat nullamo facilisis at vero eros et accumsan et iusto odio dignissim qui blandit praesent luptatum zzril delenitml augue duis dolore te feugait nulla facilisi.</p>
  <a>Read More »</a>
</div>

<div class="abs testi">
  <h2><svg width="20" height="18" viewBox="0 0 20 18"><rect x="0" y="0" width="14" height="10" rx="2" fill="#d7141a"/><path d="M3 10l0 4 4-4z" fill="#d7141a"/><rect x="7" y="5" width="13" height="9" rx="2" fill="#1e9fe0"/><path d="M17 14l0 4-4-4z" fill="#1e9fe0"/></svg>Testimonials</h2>
</div>
<div class="abs avatar" role="img" aria-label="Client portrait"></div>
<div class="abs person">Marcus Hale<small>Bussiness Man</small></div>
<div class="abs quote"><span style="color:#bbb;font-size:14px">“</span> Ut wisi enim ad minim veniam, quism nostrli erci tation ullamcorper suscipitop lobortis commodo consequat. <span style="color:#bbb;font-size:14px">”</span></div>
<div class="abs qdots"><i></i><i class="on"></i><i></i><i></i></div>

<div class="abs gallery"></div>
<div class="abs tab">Project Gallery</div>
<div class="abs arrow" style="left:91px"><svg width="8" height="10"><path d="M6 1L2 5l4 4" fill="none" stroke="#999" stroke-width="1.5"/></svg></div>
<div class="abs shot" style="left:117px" role="img" aria-label="Modern timber house lit at dusk"><div style="position:absolute;inset:0;background:linear-gradient(#6b5a3e,#c48a3e 55%,#3a3028)"></div><div class="label">Lorem ipsum dolor sit <span style="float:right;margin-right:7px">→</span></div></div>
<div class="abs shot" style="left:267px;background:linear-gradient(#9cc6ea,#4e79b0 50%,#b8bcc0)" role="img" aria-label="Blue glass office building"></div>
<div class="abs shot" style="left:418px;background:linear-gradient(#8fb8e2,#6d6a6a 50%,#a4a39f)" role="img" aria-label="Brick house with double garage"></div>
<div class="abs shot" style="left:569px;background:linear-gradient(#8fb7e0,#a2523c 50%,#5c6b4b)" role="img" aria-label="Row of new brick homes along a street"></div>
<div class="abs arrow" style="left:717px"><svg width="8" height="10"><path d="M2 1l4 4-4 4" fill="none" stroke="#999" stroke-width="1.5"/></svg></div>

<div class="abs footer"></div>
<div class="abs fline"></div>
<div class="abs fh" style="left:92px">Quick Links</div>
<div class="abs fh" style="left:240px">Contact Details</div>
<div class="abs fh" style="left:404px">Quick Contact</div>
<div class="abs social"><i style="background:#3b5998"></i><i style="background:#33b5e5"></i><i style="background:#d9261c"></i><i style="background:#f7941d"></i></div>
<div class="abs vsep" style="left:210px"></div>
<div class="abs vsep" style="left:376px"></div>
<div class="abs vsep" style="left:574px"></div>
<ul class="abs links"><li>Home</li><li>Services</li><li>Gallery</li><li>Testimonials</li><li>About Us</li><li>Contact Us</li></ul>
<div class="abs cdet"><b>123 Street Name,</b><br><b>City Name,</b> State Name,<br>Country Name - 123456</div>
<div class="abs crow" style="top:1115px"><svg width="10" height="10" viewBox="0 0 10 10"><path d="M1 1h3l1 2-1.5 1a6 6 0 003 3L8 5.5l2 1V9C5 9 1 5 1 1z" fill="#fff"/></svg>123-555-0142</div>
<div class="abs crow" style="top:1144px"><svg width="11" height="10" viewBox="0 0 11 10"><rect x="3" y="0" width="5" height="3" fill="#fff"/><rect x="0" y="3" width="11" height="5" rx="1" fill="#fff"/><rect x="3" y="6" width="5" height="4" fill="#fff" stroke="#29a8e6"/></svg>123-555-0143</div>
<div class="abs crow" style="top:1174px"><svg width="11" height="8" viewBox="0 0 11 8"><rect width="11" height="8" fill="#fff"/><path d="M0 0l5.5 4L11 0" fill="none" stroke="#29a8e6"/></svg>info@talloakbuild.com</div>
<div class="abs field" style="top:1061px">Name</div>
<div class="abs field" style="top:1086px">Email</div>
<div class="abs field" style="top:1112px;height:45px">Message</div>
<div class="abs submit">SUBMIT</div>
<div class="abs fbrand">TALL OAK</div>
<div class="abs copy">© Copyright 2015 TALLOAK<br>All Rights Reserved</div>
</body>
</html>
```